Commercial Roof Management Brochure

PDK Group www.pdkgroup-example.io is a Commercial and Industrial roof consulting company. We are looking to launch a new program to our customers. It is a roof maintenance service contract. Instead of paying for each service when needed we are bundling all the services under an annual maintenance contract. This will provide our clients with better value and service for their money. The brochure is something we would use to; email, mail or print and leave behind. It should be 1-2 pages. please incorporate our logo without the "roof and pavement consulting" text. Also include the Industry logos at the bottom somewhere BQDL and ZWT. Stick with our colour scheme from our logo and website.

Target Market(s)

Industrial and commercial property management companies, real estate holding companies, REIT companies

Industry/Entity Type

Property Maintenance

Requirements
Must have
• our logo, professional design, creates interest
Nice to have
• follow our colors from the company logo

```html
<!DOCTYPE html>
<html lang="en">
<head>
<meta charset="utf-8">
<title>PDK Group – Roof Management Brochure</title>
<link rel="stylesheet" href="https://fonts.googleapis.com/css2?family=Exo+2:wght@400;500;600&family=Lato:wght@400;700&display=swap">
<style>
  :root{
    --blue:#0d4e9a;
    --blue-deep:#0a3f80;
    --red:#e3202b;
    --red-light:#f0444c;
    --ink:#2b2b2b;
    --body:#333;
    --paper:#ffffff;
    --canvas:#ecebe8;
    --photo-a:#b9c4cc;
    --photo-b:#7a7f82;
  }
  *{box-sizing:border-box;margin:0;padding:0}
  html,body{width:1200px;height:1200px;overflow:hidden;background:var(--canvas)}
  body{position:relative;font-family:"Lato",sans-serif;color:var(--body)}
  .page{position:absolute;width:645px;height:834px;background:var(--paper);transform:scale(.8574);transform-origin:top left;overflow:hidden;box-shadow:0 6px 18px rgba(0,0,0,.18)}
  .page--cover{left:31px;top:243px}
  .page--inside{left:617px;top:243px}
  .page svg.shapes{position:absolute;left:0;top:0}

  /* cover */
  .cover__logo{position:absolute;left:34px;top:38px;display:flex;align-items:center;gap:10px;font-family:"Exo 2",sans-serif;font-weight:600;font-size:32px;letter-spacing:1px;color:var(--blue)}
  .cover__logo .mark{width:16px;height:16px;background:var(--red)}
  .cover__title{position:absolute;left:0;right:0;top:580px;text-align:center;font-family:"Exo 2",sans-serif;font-weight:500;font-size:47px;line-height:52px}
  .cover__title .l1{color:var(--red)}
  .cover__title .l2{color:var(--blue)}
  .cover__title .l3{color:var(--ink)}
  .cover__footer{position:absolute;left:0;right:0;top:795px;height:32px;display:flex;background:var(--blue);font-size:11px;color:#fff}
  .cover__footer div{display:flex;align-items:center;justify-content:center;gap:6px}
  .cover__footer .f1{width:225px}
  .cover__footer .f2{width:194px;background:var(--red)}
  .cover__footer .f3{flex:1}

  /* inside */
  .inside__heading{position:absolute;left:38px;top:35px;font-family:"Exo 2",sans-serif;font-size:14px;color:var(--blue)}
  .inside__cols{position:absolute;left:38px;top:64px;width:570px;display:flex;gap:22px;font-size:9.3px;line-height:11.4px;text-align:justify}
  .inside__cols .col{flex:1}
  .inside__cols p+p{margin-top:11.4px}
  .inside__photos{position:absolute;left:38px;top:224px;width:570px;display:flex;gap:11px}
  .inside__photos .ph{flex:1;height:163px;border:1px solid #555;background:linear-gradient(170deg,var(--photo-a),var(--photo-b))}
  .inside__photos .ph:nth-child(2){background:linear-gradient(170deg,#c9cfd3,#e6e6e6 60%,#9a9a9a)}
  .inside__photos .ph:nth-child(3){background:linear-gradient(180deg,#aeb8bf,#6d7476 55%,#3d4244)}
  .benefits{position:absolute;left:0;top:408px;width:645px;height:147px;background:var(--blue);color:#fff}
  .benefits__lead{position:absolute;left:38px;top:19px;width:575px;font-family:"Exo 2",sans-serif;font-size:12.6px;line-height:15px}
  .benefits__grid{position:absolute;left:38px;top:66px;width:575px;display:grid;grid-template-columns:1fr 1fr;column-gap:22px;row-gap:8px;font-size:9px;line-height:11px}
  .benefit{display:flex;align-items:center;gap:8px}
  .benefit svg{flex:none}
  .inside__question{position:absolute;left:38px;top:583px;width:572px;font-family:"Exo 2",sans-serif;font-size:13px;line-height:15.5px;color:var(--ink)}
  .inside__body{position:absolute;left:38px;top:630px;width:570px;font-size:8.8px;line-height:11.4px;text-align:justify;letter-spacing:-.15px}
  .inside__contact{position:absolute;right:38px;top:775px;text-align:right;color:#fff;font-size:11.5px}
  .inside__contact .row{margin-top:9px;display:flex;gap:10px;justify-content:flex-end;align-items:center;font-size:11px}
  .inside__contact .row span{display:flex;align-items:center;gap:5px}
</style>
</head>
<body>

<section class="page page--cover">
  <svg class="shapes" width="645" height="834" viewBox="0 0 645 834">
    <defs>
      <linearGradient id="photoTone" x1="0" y1="0" x2="0.6" y2="1">
        <stop offset="0" stop-color="#a9c7e3"/>
        <stop offset=".35" stop-color="#e4e0d8"/>
        <stop offset=".7" stop-color="#cf5a5f"/>
        <stop offset="1" stop-color="#b8333b"/>
      </linearGradient>
      <linearGradient id="redBand" x1="0" x2="1">
        <stop offset="0" stop-color="#e3202b"/><stop offset="1" stop-color="#f0444c"/>
      </linearGradient>
      <linearGradient id="blueBand" x1="0" x2="1">
        <stop offset="0" stop-color="#0a3f80"/><stop offset="1" stop-color="#0f5aa8"/>
      </linearGradient>
      <linearGradient id="softGrey" x1="0" y1="0" x2="0" y2="1">
        <stop offset="0" stop-color="#f3f3f3"/><stop offset="1" stop-color="#ffffff"/>
      </linearGradient>
    </defs>
    <rect x="0" y="380" width="645" height="415" fill="url(#softGrey)"/>
    <polygon points="0,0 645,0 645,290 0,275" fill="url(#photoTone)" role="img" aria-label="Photo of two roofers installing red metal roof tiles"/>
    <polygon points="0,275 645,282 645,292 164,429 0,385" fill="url(#redBand)"/>
    <polygon points="365,489 645,425 645,567" fill="url(#redBand)"/>
    <polygon points="0,385 164,429 645,292 645,407 164,547 0,497" fill="url(#blueBand)"/>
    <polygon points="0,385 164,429 164,547 0,497" fill="#0c4a92"/>
  </svg>

  <div class="cover__logo"><span class="mark"></span>PDK GROUP</div>

  <h1 class="cover__title">
    <span class="l1">Roof consulting and</span><br>
    <span class="l2">Pavement consulting</span><br>
    <span class="l3">In Toronto</span>
  </h1>

  <div class="cover__footer">
    <div class="f1">
      <svg width="11" height="11" viewBox="0 0 24 24"><path d="M6.6 10.8a15 15 0 0 0 6.6 6.6l2.2-2.2a1 1 0 0 1 1-.25 11 11 0 0 0 3.6.6 1 1 0 0 1 1 1V20a1 1 0 0 1-1 1A17 17 0 0 1 3 4a1 1 0 0 1 1-1h3.5a1 1 0 0 1 1 1 11 11 0 0 0 .6 3.6 1 1 0 0 1-.25 1z" fill="#fff"/></svg>
      416-555-0148
    </div>
    <div class="f2">
      <svg width="11" height="11" viewBox="0 0 24 24" fill="none" stroke="#fff" stroke-width="2"><circle cx="12" cy="12" r="10"/><path d="M2 12h20M12 2c3 3 3 17 0 20M12 2c-3 3-3 17 0 20"/></svg>
      www.pdkgroup-example.io
    </div>
    <div class="f3">
      <svg width="12" height="10" viewBox="0 0 24 18" fill="none" stroke="#fff" stroke-width="2"><rect x="1" y="1" width="22" height="16"/><path d="M1 1l11 9 11-9"/></svg>
      info@pdkgroup-example.io
    </div>
  </div>
</section>

<section class="page page--inside">
  <svg class="shapes" width="645" height="834" viewBox="0 0 645 834">
    <defs>
      <linearGradient id="redBand2" x1="0" x2="1">
        <stop offset="0" stop-color="#e3202b"/><stop offset="1" stop-color="#f0444c"/>
      </linearGradient>
    </defs>
    <polygon points="270,0 645,0 645,47" fill="url(#redBand2)"/>
    <polygon points="0,707 330,748 645,709 645,714 160,778 0,758" fill="url(#redBand2)"/>
    <polygon points="0,758 160,778 645,714 645,834 0,834" fill="#0d4e9a"/>
    <polygon points="0,758 160,778 160,834 0,834" fill="#0a3f80"/>
  </svg>

  <h2 class="inside__heading">Roof Management Service</h2>

  <div class="inside__cols">
    <div class="col">
      <p>When you have multiple buildings with many different tenants, managing the roofs can be a daunting process. Most of the time inspections and basic maintenance are either forgotten or put in the hands of unqualified maintenance employees or various roofers. The problem with this is that without a proper plan and management you will not get 100% return for your money or quality work.</p>
      <p>With their countless intricacies, roofs can be an overwhelming experience for real estate owners, corporations and managers. Although roofing is only a small portion of the entire investment picture it is often the costliest to replace and maintain.</p>
    </div>
    <div class="col">
      <p>PDK Group's roof operations offerings are built from the ground up, starting with the staff that you require to manage your buildings roofs. We provide roof management and inhouse consulting to enhance your current delivery model, or we can create a new operating model that will support your property management team.</p>
      <p>Our roof management capabilities provide a truly integrated approach to services from design and construction to maintenance, repairs and lifecycle management. Our roof emergency response teams are always on standby, prepared to provide demand service anywhere, any time.</p>
    </div>
  </div>

  <div class="inside__photos">
    <div class="ph" role="img" aria-label="Photo of a worker sweeping a gravel flat roof"></div>
    <div class="ph" role="img" aria-label="Photo of workers on a snow-covered flat roof"></div>
    <div class="ph" role="img" aria-label="Photo of water pooling on a flat commercial roof"></div>
  </div>

  <div class="benefits">
    <p class="benefits__lead">With PDK Group's Roof Maintenance Program, you Save Hundreds of Thousands of Dollars on repairs, replacements, inspections, consulting, maintenance, service and moisture survey!!!</p>
    <div class="benefits__grid">
      <div class="benefit">
        <svg width="22" height="22" viewBox="0 0 22 22"><circle cx="11" cy="11" r="10.5" fill="#fff"/><path d="M5 11.5L11 6l6 5.5M7 10.5V16h8v-5.5" fill="none" stroke="#0d4e9a" stroke-width="1.6"/></svg>
        We manage Real Estate Portfolios from 1 – 100 buildings
      </div>
      <div class="benefit">
        <svg width="22" height="22" viewBox="0 0 22 22"><circle cx="11" cy="11" r="10.5" fill="#fff"/><circle cx="11" cy="11" r="6" fill="none" stroke="#0d4e9a" stroke-width="1.4"/><path d="M11 7.5V11l2.5 1.5" fill="none" stroke="#0d4e9a" stroke-width="1.4"/></svg>
        Our transparent process ensures that all roofing activity is logged and available to view
      </div>
      <div class="benefit">
        <svg width="22" height="22" viewBox="0 0 22 22"><circle cx="11" cy="11" r="10.5" fill="#fff"/><rect x="6.5" y="5.5" width="9" height="11" fill="none" stroke="#0d4e9a" stroke-width="1.4"/><path d="M8.5 9h5M8.5 12h5" stroke="#0d4e9a" stroke-width="1.2"/></svg>
        1 contact for all your roofs = less confusion and faster response times
      </div>
      <div class="benefit">
        <svg width="22" height="22" viewBox="0 0 22 22"><circle cx="11" cy="11" r="10.5" fill="#fff"/><circle cx="9" cy="12" r="4" fill="none" stroke="#0d4e9a" stroke-width="1.4"/><circle cx="14" cy="10" r="4" fill="none" stroke="#0d4e9a" stroke-width="1.4"/></svg>
        Save Hundreds of Thousands of Dollars
      </div>
    </div>
  </div>

  <p class="inside__question">How would you like to spend less time worrying about project completion, cost, safety or quality, and have more time to grow your business, or other important tasks?</p>

  <p class="inside__body">A good roof maintenance program will keep tenants happy and preserve the value of your investment. By hiring us as your roof management firm you gain access to both in-house roof consulting staff, as well as their network of licensed, bonded and insured contractors who have already been vetted for good pricing and quality work. This can translate into significant savings compared to going through the yellow pages and hiring a roofer yourself. Not only is our firm able to get volume discounts on the work, we also know the contractors and understand maintenance issues such that they are capable of intelligently supervising the work.</p>

  <div class="inside__contact">
    <p>For more information or to sign up please contact PDK Group at</p>
    <div class="row">
      <span><svg width="10" height="10" viewBox="0 0 24 24"><path d="M6.6 10.8a15 15 0 0 0 6.6 6.6l2.2-2.2a1 1 0 0 1 1-.25 11 11 0 0 0 3.6.6 1 1 0 0 1 1 1V20a1 1 0 0 1-1 1A17 17 0 0 1 3 4a1 1 0 0 1 1-1h3.5a1 1 0 0 1 1 1 11 11 0 0 0 .6 3.6 1 1 0 0 1-.25 1z" fill="#e3202b"/></svg>416-555-0148</span>
      <span><svg width="12" height="9" viewBox="0 0 24 18" fill="none" stroke="#e3202b" stroke-width="2"><rect x="1" y="1" width="22" height="16"/><path d="M1 1l11 9 11-9"/></svg>info@pdkgroup-example.io</span>
      <span><svg width="11" height="11" viewBox="0 0 24 24" fill="none" stroke="#e3202b" stroke-width="2"><circle cx="12" cy="12" r="10"/><path d="M2 12h20M12 2c3 3 3 17 0 20M12 2c-3 3-3 17 0 20"/></svg>www.pdkgroup-example.io</span>
    </div>
  </div>
</section>

</body>
</html>
```